www.quillyard.com Creative Website Re-design

We are looking for multiple page designs for a client website (www.quillyard.com). The primary demographic is high school teenagers preparing for college applications. We believe the demographic is slightly skewed to female. We're looking for Home page, Content type main page (for example "All Fiction" http://www.quillyard.com/poetry/ main page would include filters to show Top Pages, Most discussed, newest etc.) User page that a content contributor could log in to see all their content, add content etc. (samples in mock ups loaded). finally an inner page for everything else.
Need to ensure there are applicable advertising spaces as per the current site.
We are looking for a fun teenage friendly design that is bright and cheerful.
Updates
Project Deadline Extended
Reason: I'm not happy with the quality of the submissions to date or the lack of submissions received. I'm hoping by extending the deadline I can find something that is workable.
Target Market(s)
high school students - primarily female - applying for college
Industry/Entity Type
Education
Number of Pages Required
4 page
Requirements
Must have
- fresh cheerful look - we need to include the ad banners & right side column similar to the current site. The sample mock up is missing those
Nice to have
- logo can be punched up

```html
<!DOCTYPE html>
<html lang="en">
<head>
<meta charset="utf-8">
<title>Quillyard — Home</title>
<link rel="stylesheet" href="https://fonts.googleapis.com/css2?family=Nunito+Sans:wght@400;600;700;800&display=swap">
<style>
:root{
  --yellow:#f8cf1f;
  --ink:#111111;
  --grey:#6d6d6d;
  --text:#333333;
  --rule:#8a8a8a;
  --pink:#f1c3c6;
  --sky:#4cbde0;
  --teal:#4bb9a6;
  --olive:#7a7458;
  --red:#e2231a;
  --white:#ffffff;
}
*{box-sizing:border-box;margin:0;padding:0}
html,body{width:1200px;height:1200px;overflow:hidden;background:#fff}
body{font-family:"Nunito Sans",sans-serif;color:var(--text)}
.page{position:absolute;left:319px;top:11px;width:702px;height:1473px;transform:scale(.8);transform-origin:0 0;background:#fff;box-shadow:0 0 6px rgba(0,0,0,.25);overflow:hidden}
.page > *{position:absolute}
.utility{top:3px;right:14px;font-size:7px;color:#444}
.logo{left:10px;top:14px;font-size:28px;font-weight:800;color:var(--yellow);letter-spacing:-.5px;line-height:1;white-space:nowrap}
.logo-dot{display:inline-block;width:8px;height:8px;background:var(--ink);border-radius:50%;margin-left:3px;vertical-align:middle}
.tagline{left:10px;top:47px;font-size:6px;color:#777;letter-spacing:.6px}
.nav{left:160px;top:16px;width:542px;height:28px;background:var(--yellow);clip-path:polygon(28px 0,100% 0,100% 100%,0 100%)}
.nav-links{right:10px;top:26px;font-size:7.5px;color:#333;white-space:nowrap}
.hero{left:0;top:44px;width:702px;height:177px;background:linear-gradient(100deg,#8f8a83,#d3cec6 30%,#c2bdb5 55%,#dcd8d2 75%,#8d8985)}
.hero-flag{left:0;top:100px;width:36px;height:76px;background:var(--ink);clip-path:polygon(0 0,100% 50%,0 100%)}
.hero-card{left:424px;top:174px;width:223px;height:47px;background:rgba(255,255,255,.85);padding:5px 9px}
.hero-card h2{font-size:12px;font-weight:700;color:#222}
.hero-card p{font-size:6.8px;line-height:1.3;color:#444}
.strip{left:0;top:221px;width:702px;height:15px;background:var(--ink);color:#fff;font-size:6px;text-align:center;line-height:15px}
.social{top:225px;width:6px;height:6px;background:#fff;border-radius:50%}
.submit{left:552px;top:221px;width:95px;height:59px;background:var(--yellow);clip-path:polygon(0 0,100% 0,100% 100%,62% 100%)}
.submit-edge{left:552px;top:221px;width:95px;height:59px;background:var(--ink);clip-path:polygon(0 0,4% 0,66% 100%,62% 100%)}
.submit-text{right:57px;top:246px;text-align:right;font-size:11px;font-weight:700;color:#222;line-height:.95;white-space:nowrap}
.submit-text small{display:block;font-size:6.5px;font-weight:400}
.feature{top:243px;height:34px;font-size:6px;line-height:1.55;color:#444;padding-left:40px}
.feature b{font-size:7.5px;color:#222;display:block}
.feature-icon{position:absolute;left:0;top:0;width:32px;height:32px;border-radius:50%;background:var(--yellow)}
.divider{top:246px;width:1px;height:28px;background:#bbb}
.section-head{height:17px;border-top:1px solid var(--rule);text-align:center;font-size:12px;font-weight:600;color:#222;line-height:15px}
.photo{overflow:hidden}
.cap{position:absolute;left:0;bottom:0;width:100%;padding:5px 9px;color:#fff;font-size:6.2px;line-height:1.45;background:linear-gradient(transparent,rgba(0,0,0,.5))}
.cap.right{text-align:right;top:0;bottom:auto;background:none}
.pager{top:531px;left:236px;font-size:0}
.pager i{display:inline-block;width:11px;height:7px;border:1px solid #777;margin-right:5px}
.pager i.on{background:var(--yellow);border-color:var(--yellow)}
.fiction-row{left:195px;width:163px;height:33px;border-bottom:1px solid #999}
.fiction-thumb{position:absolute;left:0;top:2px;width:38px;height:29px;background:linear-gradient(135deg,#2a2a2a,#777)}
.fiction-copy{position:absolute;left:42px;top:3px;width:122px;font-size:5.8px;line-height:1.55;color:#333}
.fiction-copy b{font-weight:700;color:#222}
.ad{background:var(--ink);color:#fff;font-weight:700;text-align:center}
.poem{top:817px;width:97px;height:160px;padding:5px 5px;font-size:6.2px;line-height:1.5;color:#333}
.poem h4{font-size:10.5px;font-weight:600;color:#222;line-height:1.1}
.poem .by{display:block;font-size:5.5px;color:#fff;margin-bottom:3px}
.poem .more{display:block;margin-top:2px;font-weight:800;color:#222}
.stars{display:block;color:var(--yellow);font-size:8px;letter-spacing:1px;line-height:1;margin-bottom:3px}
.review{left:502px;width:145px;font-size:6px;line-height:1.5;color:#333}
.btn{font-size:5.5px;font-weight:800;padding:1px 3px;white-space:nowrap;background:var(--red);color:#fff;border:1.5px solid #fff;outline:1px solid var(--red)}
.contest{top:1078px;width:106px;height:100px}
.footer-bar{left:0;top:1208px;width:702px;height:33px;background:var(--ink);color:#fff;font-size:6.5px;text-align:center;line-height:33px}
.footer-line{left:0;top:1241px;width:702px;height:4px;background:var(--yellow)}
.footer{left:0;top:1245px;width:702px;height:195px;background:var(--olive)}
.doodle{left:0;top:1385px;width:702px;height:55px;background:linear-gradient(90deg,#c9b34a,#8f8a55,#c8ae3f,#7d8a4e,#c9b34a)}
.foot-head{top:1264px;font-size:6px;color:#fff;letter-spacing:.3px}
.foot-head span{color:var(--yellow)}
.foot-copy{font-size:6px;line-height:1.55;color:#eee}
.copyright{left:0;top:1440px;width:702px;height:33px;background:var(--ink);color:#fff;font-size:6px;padding-left:55px;line-height:33px}
.tile-title{font-size:10px;font-weight:700;line-height:1}
.tile-copy{font-size:5.5px;line-height:1.5;margin-top:3px}
.tweet{margin-top:6px;padding-left:18px;position:relative}
.tweet i{position:absolute;left:0;top:0;width:14px;height:14px;background:#e8c552}
</style>
</head>
<body>
<div class="page">

  <div class="utility">&#9906; &nbsp;|&nbsp; Login &nbsp;|&nbsp; Signup</div>
  <div class="nav"></div>
  <div class="nav-links">Poetry &nbsp;|&nbsp; Fiction &nbsp;|&nbsp; Nonfiction &nbsp;|&nbsp; Reviews &nbsp;|&nbsp; Forums &nbsp;|&nbsp; Art &amp; Photo &nbsp;|&nbsp; Contests &nbsp;|&nbsp; Summer Programs &nbsp;|&nbsp; College Guide</div>
  <div class="logo">quillyard<span class="logo-dot"></span></div>
  <div class="tagline">for creative teens... since 1989</div>

  <div class="hero" role="img" aria-label="Photo of four smiling teenagers sitting together reading and writing in notebooks"></div>
  <div class="hero-flag"></div>
  <div class="hero-card">
    <h2>Lorem ipsum dolor sit amet</h2>
    <p>consectetur adipiscing elit. Donec in arcu massa. Maecenas ut dolor a enim luctus hendrerit.</p>
  </div>
  <div class="strip">Showcase your tallent in front of the whole world!</div>
  <div class="submit"></div>
  <div class="submit-edge"></div>
  <div class="social" style="left:589px"></div>
  <div class="social" style="left:601px"></div>
  <div class="social" style="left:613px"></div>
  <div class="submit-text">Submit<small>your work</small></div>

  <div class="feature" style="left:85px;width:170px"><div class="feature-icon"></div><b>Subscribe to Quillyard</b>monthly print magazine<br>Current issue | Past issues | Free sample</div>
  <div class="divider" style="left:251px"></div>
  <div class="feature" style="left:262px;width:150px"><div class="feature-icon"></div><b>Submit to Quillyard</b>submit your designs here<br>writing | Painting | photography</div>
  <div class="divider" style="left:405px"></div>
  <div class="feature" style="left:418px;width:150px"><div class="feature-icon"></div><b>Search Quillyard</b>articles | Painting | books | videos</div>

  <div class="section-head" style="left:55px;top:310px;width:438px">Latest articles</div>
  <div class="section-head" style="left:502px;top:310px;width:145px">Art and photo</div>

  <div class="photo" style="left:55px;top:337px;width:168px;height:184px;background:linear-gradient(160deg,#dfe3e8,#a8a39c 55%,#6f6a66)" role="img" aria-label="Photo of a group of laughing teens in a circle">
    <div class="cap">5th March | By Rory Vale<br><br>Lorem ipsum dolor sit amet, consectetur adipiscing elit.</div></div>
  <div class="photo" style="left:227px;top:337px;width:131px;height:90px;background:linear-gradient(90deg,#c0392b,#e67e22,#f1c40f,#27ae60,#2e86c1,#8e44ad)" role="img" aria-label="Photo of hands holding coloured pencils">
    <div class="cap">4th March | By Rory Vale<br><br>Lorem ipsum dolor sit amet, consectetur adipiscing elit.</div></div>
  <div class="photo" style="left:362px;top:337px;width:131px;height:90px;background:linear-gradient(120deg,#6b5a4a,#b3977a)" role="img" aria-label="Photo of students studying in a classroom">
    <div class="cap">3rd March | By Rory Vale<br><br>Lorem ipsum dolor sit amet, consectetur adipiscing elit.</div></div>
  <div class="photo" style="left:227px;top:431px;width:266px;height:90px;background:linear-gradient(90deg,#7f8e97,#b9c2c6 50%,#9aa3a6)" role="img" aria-label="Photo of a girl taking a picture with a camera">
    <div class="cap right">2nd March | By Rory Vale<br><br>Lorem ipsum dolor sit amet, consectetur adipiscing elit.</div></div>
  <div class="pager"><i></i><i class="on"></i><i></i><i></i><i></i></div>

  <div style="left:502px;top:339px;width:145px;height:150px;background:radial-gradient(circle at 50% 45%,#f9e04a 0,#f6c51d 45%,#2f8ccf 100%)" role="img" aria-label="Pop art illustration of a man looking through binoculars"></div>
  <div style="left:502px;top:489px;width:145px;height:32px;background:#f3b300;color:#fff;text-align:center;font-size:10px;font-weight:700;padding-top:5px;line-height:1">POP ART<br><span style="font-size:5.5px;font-weight:400">Painted by Mira Lenn</span></div>
  <div style="left:502px;top:521px;width:145px;height:167px;background:linear-gradient(180deg,#ededed,#cfcfcf)" role="img" aria-label="Photo of a grey printed t-shirt on a hanger"></div>
  <div style="left:502px;top:688px;width:145px;height:30px;background:#444;color:#fff;padding:3px 5px;font-size:10px;font-weight:700;line-height:1.2">SHOP CUSTOME T-SHIRT<br><span style="font-size:5.5px;font-weight:400">Buy your own designed t shirt from <b>QUILLYARD</b></span></div>

  <div class="section-head" style="left:55px;top:553px;width:303px;border-bottom:1px solid var(--rule)">Fiction</div>
  <div style="left:55px;top:581px;width:135px;height:100px;background:radial-gradient(circle at 50% 50%,#f7d51d 0,#f2c318 40%,#1a1a1a 70%)" role="img" aria-label="Hand lettered artwork about friendship"></div>
  <div style="left:55px;top:681px;width:135px;height:32px;background:var(--yellow);padding:2px 6px;font-size:5.8px;line-height:1.45;color:#333"><b>5th March | by Rory Vale</b><br>Lorem ipsum dolor sit amet, consectetur adipiscing elit. Donec in arcu massa.</div>
  <div class="fiction-row" style="top:581px"><div class="fiction-thumb" role="img" aria-label="Chalk lettering thumbnail"></div><div class="fiction-copy"><b>4th March | by Rory Vale</b><br>Lorem ipsum dolor sit amet, consectetur adipiscing elit. Donec in arcu massa.</div></div>
  <div class="fiction-row" style="top:614px"><div class="fiction-thumb" role="img" aria-label="Lettering thumbnail"></div><div class="fiction-copy"><b>3rd March | by Rory Vale</b><br>Lorem ipsum dolor sit amet, consectetur adipiscing elit. Donec in arcu massa.</div></div>
  <div class="fiction-row" style="top:647px"><div class="fiction-thumb" role="img" aria-label="Lettering thumbnail"></div><div class="fiction-copy"><b>2nd March | by Rory Vale</b><br>Lorem ipsum dolor sit amet, consectetur adipiscing elit. Donec in arcu massa.</div></div>
  <div class="fiction-row" style="top:680px;border:none"><div class="fiction-thumb" role="img" aria-label="Lettering thumbnail"></div><div class="fiction-copy"><b>1st March | by Rory Vale</b><br>Lorem ipsum dolor sit amet, consectetur adipiscing elit. Donec in arcu massa.</div></div>

  <div class="ad" style="left:55px;top:726px;width:303px;height:50px;line-height:50px;font-size:10px">Advertisement Space</div>

  <div style="left:368px;top:555px;width:125px;height:422px;border:2px solid var(--yellow);background:#fff"></div>
  <div style="left:370px;top:557px;width:121px;height:218px;background:var(--grey);color:#fff;text-align:center;font-size:9.5px;padding-top:82px;line-height:1.2">Advertisement<br>Space</div>
  <div style="left:370px;top:775px;width:121px;height:46px;background:var(--ink);color:#fff;text-align:center;font-size:12px;font-weight:600;padding-top:8px;line-height:1.3">Summer<br>programme</div>
  <div style="left:370px;top:829px;width:121px;text-align:center;font-size:6.5px;line-height:1.3;color:#222">Ready for your next<br><b>SUMMER ADVENTURE?</b></div>
  <div class="btn" style="left:407px;top:855px">LEARN MORE</div>
  <div style="left:370px;top:866px;width:121px;height:109px;background:linear-gradient(180deg,#7fa85e,#5a9bd0 60%,#2f6fb0)" role="img" aria-label="Photo of two children paddling a kayak"></div>

  <div class="section-head" style="left:55px;top:788px;width:303px;border-bottom:1px solid var(--rule)">Poetry</div>
  <div class="poem" style="left:55px;background:var(--pink)"><h4>MAKE BELIEVE</h4><span class="by">By Tessa K., Dover, OH</span>We were doomed from the beginning,<br>Blinded from the start,<br>But nothing can be done<br>To fool a happy heart.<br>With each smile and giggle,<br>Every embrace and every kiss,<br>We were shooting toward a happy ending,<br>And we missed.<span class="more">READ MORE</span></div>
  <div class="poem" style="left:157px;background:var(--sky)"><h4>I TAKE BACK MY TEARS</h4><span class="by">By Nora P., Alder, GA</span>I take back my tears<br>the wasted years<br>I spent crying<br>for what never could happen<br>I take back my heart<br>my shattered heart<br>Up off the ground.<br>And we missed.<span class="more">READ MORE</span></div>
  <div class="poem" style="left:260px;width:98px;background:var(--teal)"><h4>REM SLEEP</h4><span class="by">By JuneR, Brookvale, CO</span>You can dream more.<br>The earth balances<br>precariously, but in your<br>soft moments of slumber,<br>the world is yours.<br>Explore.<br>fine poppy seeds fall<br>slowly down<br>the curtain of your eyelids.<br>And we missed.<span class="more">READ MORE</span></div>

  <div class="section-head" style="left:502px;top:737px;width:145px;border-bottom:1px solid var(--rule)">Reviews</div>
  <div class="review" style="top:760px"><span class="stars">★★★★★</span>Lorem ipsum dolor sit amet, consectetur adipiscing elit. Donec in arcu massa. Maecenas</div>
  <div class="review" style="top:797px"><span class="stars">★★★★★</span>Lorem ipsum dolor sit amet, consectetur adipiscing elit. Donec in arcu massa. Maecenas</div>
  <div class="review" style="top:832px"><span class="stars">★★★★★</span>Lorem ipsum dolor sit amet, consectetur adipiscing elit. Donec in arcu massa. Maecenas</div>
  <div class="review" style="top:870px"><span class="stars">★★★★★</span>Lorem ipsum dolor sit amet, consectetur adipiscing elit. Donec in arcu massa. Maecenas</div>
  <div class="review" style="top:905px"><span class="stars">★★★★★</span>Lorem ipsum dolor sit amet, consectetur adipiscing elit. Donec in arcu massa. Maecenas</div>

  <div class="section-head" style="left:502px;top:952px;width:145px;border-bottom:1px solid var(--rule)">Forums</div>
  <div style="left:502px;top:977px;width:69px;height:75px;background:#6a6660;color:#fff;padding:4px 5px;text-align:center">
    <div class="tile-title">WRITERS'<br>WORKSHOP</div>
    <div class="tile-copy">Where teen writers<br>share their work</div></div>
  <div class="btn" style="left:512px;top:1033px">LEARN MORE</div>
  <div style="left:576px;top:977px;width:71px;height:75px;background:var(--sky);color:#111;padding:4px 5px;text-align:center">
    <div class="tile-title">REGULAR<br><span style="letter-spacing:3px;font-size:8px">FORUMS</span></div>
    <div class="tile-copy">Lively discussions<br>with other teens</div></div>
  <div class="btn" style="left:587px;top:1033px">LEARN MORE</div>

  <div class="ad" style="left:55px;top:986px;width:438px;height:50px;line-height:50px;font-size:10px">Advertisement Space</div>

  <div class="section-head" style="left:55px;top:1047px;width:438px;border-bottom:1px solid var(--rule)">Latest contests</div>
  <div class="contest" style="left:55px;background:linear-gradient(135deg,#f26d9c,#f4d23a 60%,#222)" role="img" aria-label="Pop art illustration for the cover art contest"></div>
  <div style="left:102px;top:1081px;font-size:8px;color:#222;line-height:1">COVER ART<br><span style="color:var(--red);font-size:6px;letter-spacing:1.5px">CONTEST</span></div>
  <div class="contest" style="left:166px;background:linear-gradient(180deg,#f4c59b,#e48f5f)" role="img" aria-label="Watercolour background with poetry lettering"></div>
  <div style="left:168px;top:1083px;width:104px;font-size:5.5px;color:#7a3a1e;text-align:center;line-height:1.3">SERIOUS, FUNNY, LONG OR SHORT<br>SEND US YOUR POEMS TODAY</div>
  <div class="contest" style="left:277px;background:linear-gradient(160deg,#3f1e1e,#a9473a)" role="img" aria-label="Photo of an open book with pages folded into a heart"></div>
  <div style="left:281px;top:1081px;font-size:11px;color:#fff;line-height:1">FICTION<br><span style="font-size:6px;letter-spacing:2px">CONTEST</span></div>
  <div class="contest" style="left:388px;background:linear-gradient(90deg,#f3f3f3,#bdbdbd)" role="img" aria-label="Photo of a girl wearing headphones"></div>
  <div style="left:391px;top:1084px;font-size:6px;color:#222;line-height:1.2"><b>TRAVEL &amp; CULTURE<br>CONTEST</b><br><span style="color:var(--red);font-size:5.3px">describe your latest<br>cultural adventures</span></div>

  <div class="section-head" style="left:502px;top:1070px;width:145px;border-bottom:1px solid var(--rule)">College guide</div>
  <div style="left:502px;top:1099px;width:145px;height:79px;background:linear-gradient(135deg,#3fc1c9,#7fd0c8 40%,#f2c94c 75%,#e9e4da)" role="img" aria-label="Photo of a desk with books and glasses"></div>
  <div style="left:508px;top:1104px;font-size:6px;letter-spacing:2px;color:#222">your best</div>
  <div style="left:508px;top:1115px;font-size:11px;font-weight:600;color:#222;line-height:1.1">COLLEGE<br>GUIDE</div>
  <div class="btn" style="left:509px;top:1149px">LEARN MORE</div>

  <div class="footer-bar">Home &nbsp;|&nbsp; Blog &nbsp;|&nbsp; Shop &nbsp;|&nbsp; Contact Us</div>
  <div class="footer-line"></div>
  <div class="footer"></div>
  <div class="doodle" role="img" aria-label="Decorative band of colourful hand drawn doodles"></div>

  <div class="logo" style="left:55px;top:1268px;font-size:26px">quillyard<span class="logo-dot"></span></div>
  <div class="tagline" style="left:55px;top:1297px;color:#ddd">for creative teens... since 1989</div>
  <div style="left:57px;top:1315px;width:7px;height:7px;border-radius:50%;background:var(--ink)"></div>
  <div style="left:91px;top:1315px;width:7px;height:7px;border-radius:50%;background:var(--ink)"></div>
  <div style="left:128px;top:1315px;width:7px;height:7px;border-radius:50%;background:var(--ink)"></div>
  <div class="foot-copy" style="left:55px;top:1333px;width:120px">Lorem ipsum dolor sit amet, consectetur adipiscing elit. Donec in arcu massa. Maecenas ut dolor a enim luctus hendrerit. Pellentesque</div>
  <div style="left:55px;top:1378px;font-size:7.5px;font-weight:700;color:#fff">Subscribe our newsletter</div>
  <div style="left:55px;top:1394px;width:105px;height:14px;background:var(--ink)"></div>
  <svg style="left:146px;top:1397px" width="9" height="8" viewBox="0 0 9 8"><path d="M0 4 9 0 6 8 4 5Z" fill="#f8cf1f"/></svg>

  <div class="foot-head" style="left:213px">FOLLOW US ON <span>CHATTER</span></div>
  <div style="left:213px;top:1276px;width:112px;height:132px;background:#fff;border:1px solid #ccc;padding:4px 5px;font-size:5px;line-height:1.45;color:#444">
    <div style="font-size:6.5px;font-weight:700;color:#222;border-bottom:1px solid #ddd;padding-bottom:2px">Updates</div>
    <div class="tweet"><i></i><b>Quillyard</b><br>Lorem ipsum dolor sit amet, consectetur adipiscing elit, sed diam nonummy nibh euismod.</div>
    <div class="tweet"><i></i><b>Quillyard</b><br>Lorem ipsum dolor sit amet, consectetur adipiscing elit, sed diam nonummy nibh euismod.</div>
  </div>

  <div class="foot-head" style="left:376px">LIKE US ON <span>FRIENDWALL</span></div>
  <div style="left:376px;top:1276px;width:105px;height:100px;background:#fff;border:1px solid #ccc"></div>
  <div style="left:377px;top:1277px;width:103px;height:47px;background:linear-gradient(135deg,#3f6b2f,#9a2b22)" role="img" aria-label="Page cover photo of a coffee cup"></div>
  <div style="left:380px;top:1330px;width:96px;font-size:4.8px;color:#555">You and 36 other friends like this</div>
  <div style="left:380px;top:1340px;width:96px;height:26px;background:linear-gradient(90deg,#5a6f9c,#c77b52,#7a9c5a,#4a5c8a)" role="img" aria-label="Row of follower avatars"></div>

  <div class="foot-head" style="left:529px">CONTACT <span>US</span></div>
  <div style="left:529px;top:1278px;width:118px;height:56px;background:linear-gradient(135deg,#eceae6,#d9d7d2)" role="img" aria-label="Street map showing the office location"></div>
  <svg style="left:529px;top:1345px" width="6" height="8" viewBox="0 0 6 8"><path d="M3 0a3 3 0 0 1 3 3c0 2-3 5-3 5S0 5 0 3a3 3 0 0 1 3-3z" fill="#111"/></svg>
  <div class="foot-copy" style="left:540px;top:1344px">Quillyard, Box 12, Fairview,<br>ME 04011</div>
  <svg style="left:529px;top:1371px" width="6" height="7" viewBox="0 0 6 7"><rect x="1" width="4" height="7" rx="1" fill="#111"/></svg>
  <div class="foot-copy" style="left:540px;top:1369px">(555) 014-2290</div>
  <svg style="left:529px;top:1386px" width="7" height="5" viewBox="0 0 7 5"><rect width="7" height="5" fill="#111"/><path d="M0 0 3.5 3 7 0" stroke="#fff" stroke-width=".6" fill="none"/></svg>
  <div class="foot-copy" style="left:540px;top:1383px">editor@quillyard.com</div>

  <div class="copyright">Copyright © Quillyard. All Rights Reserved.</div>
</div>
</body>
</html>
```